Industrial/Commercial Plumbing Capability Statement

Would like a construction capability statement/Brochure amended to be similar to the attached. -
Have included photos and Notes on the attached
would like project photos to be used
This is a previous capability statement that we would like amended and altered to include, safety, QA and Recent Projects
Please use our company logo
Updates

Need extra days to review

Target Market(s)

Construction work - Industrial

Industry/Entity Type

Plumbing

Requirements
Must have
• Include all items in contents page

Eye Catching Photos relevant to construction industry and relevant to topic on page

```html
<!DOCTYPE html>
<html lang="en">
<head>
<meta charset="utf-8">
<title>Keystone Plumbers — Capability Statement</title>
<link href="https://fonts.googleapis.com/css2?family=Montserrat:wght@300;400;500;600;700;800&display=swap" rel="stylesheet">
<style>
:root{
  --navy:#0b4a6b;
  --ink:#4a4f55;
  --grey-tab:#4b4f54;
  --canvas:#d4d7da;
  --white:#ffffff;
}
*{box-sizing:border-box;margin:0;padding:0}
html,body{width:1200px;height:2293px;overflow:hidden}
body{background:var(--canvas);font-family:'Montserrat',sans-serif;color:var(--ink);position:relative}

.page{position:absolute;width:316px;height:409px;background:var(--white);overflow:hidden}
.page.navy{background:var(--navy)}
.cover-large{left:284px;top:60px;transform:scale(2.0);transform-origin:top left;box-shadow:0 3px 8px rgba(0,0,0,.15)}

.photo{position:absolute}
.photo.skyline{background:linear-gradient(180deg,#7fb3e6 0%,#a9cdee 38%,#c3d6e4 52%,#6f8496 62%,#8c9aa6 72%,#5f7ea6 80%,#3e5f8a 100%)}
.photo.engineer{background:radial-gradient(ellipse 30% 45% at 38% 55%,#e8883a 0%,rgba(232,136,58,0) 100%),linear-gradient(90deg,#d7dfe6 0%,#c6cfd6 45%,#8f989e 75%,#6c757b 100%)}
.photo.hardhat{background:radial-gradient(ellipse 38% 60% at 50% 60%,#f0c42a 0%,#e2b43a 40%,rgba(226,180,58,0) 75%),linear-gradient(180deg,#9fb9cf 0%,#c9d6df 45%,#c8b59a 100%)}
.photo.building{background:linear-gradient(180deg,#a9c3d8 0%,#d5dde3 30%,#8e9aa3 60%,#5d6a73 100%)}
.photo.worker{background:radial-gradient(ellipse 22% 18% at 50% 35%,#f2b928 0%,rgba(242,185,40,0) 100%),radial-gradient(ellipse 35% 30% at 50% 78%,#3f5f95 0%,rgba(63,95,149,0) 100%),linear-gradient(180deg,#6fa7de 0%,#a5c8ea 50%,#c6daee 100%)}

.heading{position:absolute;left:32px;top:46px;border-left:1.5px solid var(--navy);padding-left:9px;line-height:1.05}
.heading .light{display:block;font-weight:300;font-size:14px;color:var(--navy);letter-spacing:.3px}
.heading .bold{display:block;font-weight:800;font-size:18.5px;color:var(--navy)}
.navy .heading{border-color:var(--white)}
.navy .heading .light,.navy .heading .bold{color:var(--white)}

.body{position:absolute;left:32px;right:34px;font-size:4.6px;line-height:1.5;color:var(--ink)}
.body p{margin-bottom:3.4px}
.body .pull{font-size:7.2px;font-weight:600;color:var(--navy);line-height:1.25;border-left:1.2px solid var(--navy);padding-left:7px;margin:6px 0}

.footer{position:absolute;left:32px;right:30px;bottom:18px;display:flex;align-items:center;gap:5px}
.footer .site{font-size:4.6px;font-weight:700;color:var(--navy)}
.footer .line{flex:1;height:.7px;background:var(--navy)}
.footer .num{width:9px;height:9px;border:.7px solid var(--navy);border-radius:50%;font-size:4px;font-weight:700;color:var(--navy);display:flex;align-items:center;justify-content:center}
.navy .footer .site,.navy .footer .num{color:var(--white);border-color:var(--white)}
.navy .footer .line{background:var(--white)}

.brand{display:flex;align-items:center;gap:4px;font-weight:800;color:var(--white);font-size:12px;letter-spacing:.2px;white-space:nowrap}
.brand .mark{width:9px;height:9px;background:var(--white)}
.brand.on-white{color:var(--navy)}
.brand.on-white .mark{background:var(--navy)}

/* cover */
.cover .photo{left:9px;top:9px;width:297px;height:390px}
.cover svg.panel{position:absolute;left:0;top:0}
.cover .vertical-site{position:absolute;right:17px;top:60px;transform:rotate(-90deg) translateX(-50%);transform-origin:right top;font-size:6px;letter-spacing:.6px;color:#2a3a48;white-space:nowrap}
.cover .vertical-site b{font-weight:700}
.cover .vline{position:absolute;right:19px;top:9px;width:.6px;height:42px;background:#2a3a48}
.cover .title{position:absolute;left:32px;top:304px;border-left:1.5px solid var(--white);padding-left:9px;line-height:1;color:var(--white)}
.cover .title .light{display:block;font-weight:300;font-size:16px}
.cover .title .bold{display:block;font-weight:800;font-size:23px}
.cover .brand{position:absolute;left:43px;top:370px}

/* contents */
.toc{position:absolute;left:42px;right:42px;top:150px;list-style:none}
.toc li{display:flex;align-items:baseline;font-size:6px;font-weight:600;color:var(--white);letter-spacing:.2px;height:19px}
.toc .label{width:88px}
.toc .dots{flex:1;border-bottom:.8px dotted rgba(255,255,255,.7);margin:0 5px}

.signatures{position:absolute;left:40px;right:60px;top:364px;display:flex;justify-content:space-between;font-size:6.5px;font-weight:500;color:var(--navy)}

/* about */
.feature{position:absolute;left:32px;right:34px;top:208px;height:95px;background:var(--navy);display:flex}
.feature .text{width:55%;padding:8px 10px;font-size:4.3px;line-height:1.45;color:var(--white)}
.feature .text p{margin-bottom:4px}
.feature .photo{position:relative;flex:1}

/* quote */
.quote-page .photo{left:0;top:0;width:316px;height:281px}
.quote-box{position:absolute;left:32px;right:36px;top:228px;height:118px;background:var(--navy);border-radius:4px;color:var(--white)}
.quote-box .inner{border:.7px solid rgba(255,255,255,.8);border-top:none;position:absolute;inset:12px 12px 12px 12px}
.quote-box p{position:absolute;left:22px;right:22px;top:32px;font-size:5.6px;font-weight:600;line-height:1.38}
.quote-box .open,.quote-box .close{position:absolute;font-size:28px;font-weight:800;line-height:1;background:var(--navy);padding:0 3px}
.quote-box .open{left:16px;top:2px}
.quote-box .close{right:20px;bottom:-4px}
.quote-page .brand{position:absolute;right:36px;top:358px;font-size:10px}

/* services */
.service{position:absolute;left:32px;right:34px}
.service .tab{position:relative;height:11px;border-bottom:.8px solid var(--grey-tab)}
.service .tab span{position:absolute;left:0;top:0;height:11px;width:122px;background:var(--grey-tab);color:var(--white);font-size:7px;font-weight:800;padding-left:6px;line-height:11px;clip-path:polygon(0 0,92% 0,100% 100%,0 100%)}
.service .row{display:flex;gap:12px;margin-top:6px}
.service .icon{width:55px;height:56px;background:var(--navy);display:flex;align-items:center;justify-content:center;flex:none}
.service ul{list-style:none;font-size:4.8px;font-weight:700;color:var(--navy);line-height:1.45;width:88px;margin-top:3px}
.service li::before{content:"» "}

/* health */
.health-page .photo{left:32px;top:168px;width:250px;height:118px;border-radius:3px}

/* contact */
.contact-page .photo{left:9px;top:9px;width:298px;height:392px}
.contact-page svg.panel{position:absolute;left:0;top:0}
.contact-block{position:absolute;left:199px;top:293px;color:var(--white)}
.contact-block .label{border-left:1.2px solid var(--white);padding-left:7px;font-size:11px;font-weight:300;margin-bottom:7px;white-space:nowrap}
.contact-block .label b{font-weight:800}
.contact-block .item{display:flex;gap:5px;font-size:5px;line-height:1.4;margin-bottom:3px;white-space:nowrap}
.contact-block svg{flex:none;margin-top:.5px}
.contact-page .brand{position:absolute;right:27px;top:375px;font-size:10px}
</style>
</head>
<body>

<section class="page cover cover-large" aria-label="Cover">
  <div class="photo skyline" role="img" aria-label="City skyline of office towers beside a river under a clear blue sky"></div>
  <div class="vline"></div>
  <div class="vertical-site">www.<b>keystoneplumbers</b>.com.au</div>
  <svg class="panel" width="316" height="409" viewBox="0 0 316 409"><polygon points="0,228 276,409 0,409" fill="var(--navy)"/></svg>
  <div class="title"><span class="light">CAPABILITY</span><span class="bold">STATEMENT</span></div>
  <div class="brand"><span class="mark"></span>KEYSTONE PLUMBERS.</div>
</section>

<section class="page cover" style="left:75px;top:995px" aria-label="Cover">
  <div class="photo skyline" role="img" aria-label="City skyline of office towers beside a river under a clear blue sky"></div>
  <div class="vline"></div>
  <div class="vertical-site">www.<b>keystoneplumbers</b>.com.au</div>
  <svg class="panel" width="316" height="409" viewBox="0 0 316 409"><polygon points="0,228 276,409 0,409" fill="var(--navy)"/></svg>
  <div class="title"><span class="light">CAPABILITY</span><span class="bold">STATEMENT</span></div>
  <div class="brand"><span class="mark"></span>KEYSTONE PLUMBERS.</div>
</section>

<section class="page navy" style="left:447px;top:995px" aria-label="Table of contents">
  <div class="heading"><span class="light">TABLE OF</span><span class="bold">CONTENTS</span></div>
  <ul class="toc">
    <li><span class="label">FROM THE DIRECTORS</span><span class="dots"></span>01</li>
    <li><span class="label">ABOUT THE BUSINESS</span><span class="dots"></span>01</li>
    <li><span class="label">OUR SERVICES</span><span class="dots"></span>01</li>
    <li><span class="label">HEALTH AND SAFETY</span><span class="dots"></span>01</li>
    <li><span class="label">QUALITY ASSURANCE</span><span class="dots"></span>01</li>
    <li><span class="label">RECENT PROJECTS</span><span class="dots"></span>01</li>
    <li><span class="label">KP DATA</span><span class="dots"></span>01</li>
    <li><span class="label">MEET THE TEAM</span><span class="dots"></span>01</li>
  </ul>
  <div class="footer"><span class="site">www.keystoneplumbers.com.au</span><span class="line"></span><span class="num">02</span></div>
</section>

<section class="page" style="left:824px;top:995px" aria-label="Message from the directors">
  <div class="heading"><span class="light">MESSAGE FROM</span><span class="bold">THE DIRECTORS</span></div>
  <div class="body" style="top:98px">
    <p>Our modern approach to plumbing construction means every project benefits from current materials, proven methods and industry developments. As specialists in high quality construction, commercial maintenance and retail fit-outs, we stand at the forefront of plumbing in the region.</p>
    <p>Our practical approach keeps us ahead of the field and shows our skill and experience in delivering the right products and installation methods for your projects.</p>
    <p class="pull">We work closely with our Builders on the scope of works, to guarantee that targets are met, and exceeded.</p>
    <p>Our team has broad expertise across many areas, from new retail centres and hospitals to industrial equipment.</p>
    <p>We aim to exceed the expectations of our customers and have a proven record of delivering large projects on time and on budget, and we believe it is our job to make your project a success.</p>
    <p class="pull">We pride ourselves on having the highest level of quality on-site management in the industry, displaying expert communication, effective collaboration and unmatched problem solving skills. We stand steadfast upon our reputation as problem solvers and innovative and flexible service providers.</p>
    <p>With the right team you can avoid costly and needless delays. When you work with us, you know you are dealing with trusted specialists in commercial plumbing.</p>
    <p>We look forward to working with you.</p>
  </div>
  <div class="signatures"><span>Daniel Hart</span><span>Marco Bellini</span></div>
  <div class="footer"><span class="site">www.keystoneplumbers.com.au</span><span class="line"></span><span class="num">03</span></div>
</section>

<section class="page" style="left:75px;top:1419px" aria-label="About the business">
  <div class="heading"><span class="light">ABOUT</span><span class="bold">THE BUSINESS</span></div>
  <div class="body" style="top:98px">
    <p>Founded in 2004 by our two managing directors, we specialise in the commercial sector with wide experience across all levels of the industry, from new retail centres, hotels and high-rise developments to hospitals and industrial plant.</p>
    <p>Strong supplier relationships are key to our business. We keep close working ties with major plumbing suppliers so we stay at the forefront of advances in both products and plumbing techniques.</p>
    <p>We balance cost-effective plumbing with the highest standards in the industry. Our approach is built on cooperation, innovation, integrity and accountability at every stage of the work, and on the relationships we build with customers, colleagues and stakeholders.</p>
  </div>
  <div class="feature">
    <div class="text">
      <p>We believe excellent customer relations, a passion for the industry and real expertise let us deliver what we promise. This sets us apart, as satisfied customers keep coming back and recommend us to others.</p>
      <p>Our success depends on the quality of our people. We are committed to attracting and keeping talented staff by providing a strong platform for ongoing career development.</p>
    </div>
    <div class="photo building" role="img" aria-label="Modern multi-storey commercial building with balconies"></div>
  </div>
  <div class="body" style="top:312px">
    <p>We employ a highly skilled team of full-time staff, from fully qualified tradespeople to apprentices and office personnel. We are committed to regular training and cross-skilling of all our staff and promote a workplace that supports career advancement and personal growth.</p>
  </div>
  <div class="footer"><span class="site">www.keystoneplumbers.com.au</span><span class="line"></span><span class="num">04</span></div>
</section>

<section class="page quote-page" style="left:447px;top:1419px" aria-label="Client testimonial">
  <div class="photo engineer" role="img" aria-label="Site engineer in white hard hat and orange hi-vis vest holding plans and a tablet in front of a building under construction"></div>
  <div class="quote-box">
    <div class="inner"></div>
    <span class="open">“</span>
    <p>As commercial Builders we often have to work on difficult Projects that require unique, innovative results. Keystone Plumbers are problem solvers and work closely with our team to deliver high quality solution oriented Projects. We started working with Keystone Plumbers several years ago and continue to be impressed by their professionalism and attention to detail.</p>
    <span class="close">”</span>
  </div>
  <div class="brand on-white"><span class="mark"></span>KEYSTONE PLUMBERS.</div>
  <div class="footer"><span class="site">www.keystoneplumbers.com.au</span><span class="line"></span><span class="num">05</span></div>
</section>

<section class="page" style="left:824px;top:1419px" aria-label="Our services">
  <div class="heading"><span class="light">OUR</span><span class="bold">SERVICES</span></div>
  <div class="service" style="top:102px">
    <div class="tab"><span>CONSTRUCTION</span></div>
    <div class="row">
      <div class="icon"><svg width="30" height="36" viewBox="0 0 30 36" fill="none" stroke="#fff" stroke-width="1.3"><rect x="3" y="10" width="11" height="24"/><rect x="16" y="4" width="11" height="30"/><path d="M6 15h5M6 20h5M6 25h5M19 9h5M19 14h5M19 19h5M19 24h5M0 34h30"/></svg></div>
      <ul><li>Airports</li><li>Apartments /<br>&nbsp;&nbsp;Mixed Use Developments</li><li>Commercial Fitouts</li><li>Defence &amp; Government</li><li>Education</li><li>Fire Services</li></ul>
      <ul><li>Hotels</li><li>Health</li><li>HVAC - Cooling Towers</li><li>Multi Storey Office Blocks</li><li>Retail</li><li>Sporting /<br>&nbsp;&nbsp;Recreation Facilities</li></ul>
    </div>
  </div>
  <div class="service" style="top:197px">
    <div class="tab"><span>MAINTENANCE</span></div>
    <div class="row">
      <div class="icon"><svg width="32" height="32" viewBox="0 0 32 32" fill="none" stroke="#fff" stroke-width="1.5" stroke-linejoin="round"><path d="M21 3a7 7 0 0 0-6.5 9.5L4 23a3 3 0 0 0 4.2 4.2L18.7 16.7A7 7 0 0 0 28 10l-4 4-4-1-1-4 4-4a7 7 0 0 0-2-2z"/></svg></div>
      <ul><li>24/7 Assistance</li><li>Backflow Devices</li><li>Blocked Drains</li><li>Gas and Water Leaks</li><li>Hot Water Systems</li><li>Preventative<br>&nbsp;&nbsp;Maintenance Programs</li></ul>
      <ul><li>Pump Systems</li><li>Reactive</li><li>Roof Leaks</li><li>Servicing</li><li>Thermostatic<br>&nbsp;&nbsp;Mixing Valves</li></ul>
    </div>
  </div>
  <div class="service" style="top:292px">
    <div class="tab"><span>SURVEYING</span></div>
    <div class="row">
      <div class="icon"><svg width="30" height="34" viewBox="0 0 30 34" fill="none" stroke="#fff" stroke-width="1.4"><rect x="9" y="2" width="12" height="10" rx="1.5"/><circle cx="15" cy="7" r="2"/><path d="M15 12v4M15 16L6 33M15 16v17M15 16l9 17"/></svg></div>
      <ul><li>Annual Testing</li><li>Audits</li><li>Budget Assistance</li><li>Capital Asset Reports</li><li>CCTV</li></ul>
      <ul><li>Design Assistance</li><li>Pipe Locating</li><li>Pipework Surveying</li><li>Preliminary Investigations</li><li>Water Saving</li></ul>
    </div>
  </div>
  <div class="footer"><span class="site">www.keystoneplumbers.com.au</span><span class="line"></span><span class="num">06</span></div>
</section>

<section class="page health-page" style="left:75px;top:1848px" aria-label="Health, safety and environment">
  <div class="heading"><span class="light">HEALTH SAFETY &amp;</span><span class="bold">ENVIRONMENT</span></div>
  <div class="body" style="top:100px">
    <p>The health and safety of all Keystone Plumbers employees is essential, and a goal that must not be compromised.</p>
    <p>Keystone Plumbers has a solid reputation for building strong business relationships with our clients, and this has been helped by our responsible approach to safety on the job.</p>
    <p>We take our employees' and clients' safety seriously and take a proactive approach to health and safety policies by setting clear guidelines.</p>
  </div>
  <div class="photo hardhat" role="img" aria-label="Yellow hard hat and work gloves resting on a ledge with cranes behind"></div>
  <div class="body" style="top:302px">
    <p>Every site begins with a full risk review, daily toolbox talks and clear incident reporting, so each worker understands the hazards around them. We check equipment, review methods after each stage and share lessons across teams, so everyone on site goes home safe at the end of every shift.</p>
  </div>
  <div class="footer"><span class="site">www.keystoneplumbers.com.au</span><span class="line"></span><span class="num">07</span></div>
</section>

<section class="page contact-page" style="left:447px;top:1848px" aria-label="Contact us">
  <div class="photo worker" role="img" aria-label="Smiling construction worker in yellow hard hat and safety glasses with a tower crane behind"></div>
  <svg class="panel" width="316" height="409" viewBox="0 0 316 409"><polygon points="316,252 316,409 40,409" fill="var(--navy)"/></svg>
  <div class="contact-block">
    <div class="label">CONTACT <b>US</b></div>
    <div class="item"><svg width="5" height="6" viewBox="0 0 10 12"><path d="M5 0a4 4 0 0 1 4 4c0 3-4 8-4 8S1 7 1 4a4 4 0 0 1 4-4z" fill="none" stroke="#fff" stroke-width="1.2"/><circle cx="5" cy="4" r="1.3" fill="#fff"/></svg><span>14 Harbour Rd,<br>Westfield WA 6000</span></div>
    <div class="item"><svg width="5" height="6" viewBox="0 0 10 12"><rect x="2" y="1" width="6" height="10" rx="1.2" fill="none" stroke="#fff" stroke-width="1.2"/><circle cx="5" cy="9" r=".8" fill="#fff"/></svg><span>(08) 9000 4120</span></div>
    <div class="item"><svg width="6" height="6" viewBox="0 0 12 12"><circle cx="6" cy="6" r="5" fill="none" stroke="#fff" stroke-width="1.1"/><path d="M1 6h10M6 1c2.5 3 2.5 7 0 10M6 1c-2.5 3-2.5 7 0 10" fill="none" stroke="#fff" stroke-width=".9"/></svg><span>www.keystoneplumbers.com.au</span></div>
  </div>
  <div class="brand"><span class="mark"></span>KEYSTONE PLUMBERS.</div>
</section>

</body>
</html>
```